Investment company needing business card

We are wanting a business card which looks sharp and easy on the eye. We are thinking of having a business card with the logo embossed on it, to really make it stand out. We will only have a small amount of information of the business card, person's name, position, email address and phone number

Contact Information for Business Card

Danica Pruett
Executive Assistant
+64 21 547 3162
danicap@harwellcapital.co.nz

Requirements
Must have
• Embossed logo
Should not have
• Not to be busy

```html
<!DOCTYPE html>
<html lang="en">
<head>
<meta charset="utf-8">
<title>Harwell Capital – Business Card</title>
<link href="https://fonts.googleapis.com/css2?family=Roboto:wght@400;500;700&display=swap" rel="stylesheet">
<style>
  :root {
    --backdrop: #e9eaea;
    --card-green: #23b06c;
    --card-charcoal: #333335;
    --ink-dark: #23352b;
    --ink-green: #2bb56f;
    --shadow: 0 10px 28px rgba(0,0,0,0.18);
  }
  * { box-sizing: border-box; margin: 0; padding: 0; }
  html, body {
    width: 1200px; height: 800px; overflow: hidden;
    background: var(--backdrop);
    font-family: "Roboto", Arial, sans-serif;
  }
  .canvas { position: relative; width: 1200px; height: 800px; }

  .card {
    position: absolute;
    width: 580px; height: 331px;
    box-shadow: var(--shadow);
  }
  .card--green { left: 150px; top: 50px; background: var(--card-green); color: var(--ink-dark); }
  .card--charcoal { left: 470px; top: 419px; background: var(--card-charcoal); color: var(--ink-green); }

  .brand {
    position: absolute; left: 62px; top: 82px;
    display: flex; align-items: center; gap: 12px;
  }
  .brand__mark { width: 30px; height: 30px; background: currentColor; }
  .brand__name {
    font-size: 26px; font-weight: 500; letter-spacing: 2px; text-transform: uppercase;
  }

  .contact {
    position: absolute; left: 318px; top: 160px;
  }
  .contact__name {
    font-size: 19px; font-weight: 700; text-transform: uppercase; letter-spacing: 0.2px;
  }
  .contact__role {
    font-size: 15px; font-weight: 400; margin: 3px 0 10px 6px;
  }
  .contact__line {
    display: flex; align-items: center; gap: 10px;
    font-size: 15px; font-weight: 400; margin-top: 6px;
  }
  .contact__icon { width: 14px; height: 14px; fill: currentColor; flex: none; }
</style>
</head>
<body>
<main class="canvas">

  <section class="card card--green" aria-label="Business card, green side">
    <div class="brand">
      <span class="brand__mark"></span>
      <span class="brand__name">Harwell Capital</span>
    </div>
    <div class="contact">
      <p class="contact__name">Danica Pruett</p>
      <p class="contact__role">Executive Assistant</p>
      <p class="contact__line">
        <svg class="contact__icon" viewBox="0 0 24 24" aria-hidden="true"><path d="M6.6 10.8a15.1 15.1 0 0 0 6.6 6.6l2.2-2.2a1 1 0 0 1 1-.25 11.4 11.4 0 0 0 3.6.57 1 1 0 0 1 1 1V20a1 1 0 0 1-1 1A17 17 0 0 1 3 4a1 1 0 0 1 1-1h3.5a1 1 0 0 1 1 1c0 1.25.2 2.45.57 3.57a1 1 0 0 1-.25 1z"/></svg>
        <span>+64 21 547 3162</span>
      </p>
      <p class="contact__line">
        <svg class="contact__icon" viewBox="0 0 24 24" aria-hidden="true"><path d="M2 5h20v14H2zm2 2v.5l8 5 8-5V7zm0 2.8V17h16V9.8l-8 5z"/></svg>
        <span>danicap@harwellcapital.co.nz</span>
      </p>
    </div>
  </section>

  <section class="card card--charcoal" aria-label="Business card, charcoal side">
    <div class="brand">
      <span class="brand__mark"></span>
      <span class="brand__name">Harwell Capital</span>
    </div>
    <div class="contact">
      <p class="contact__name">Danica Pruett</p>
      <p class="contact__role">Executive Assistant</p>
      <p class="contact__line">
        <svg class="contact__icon" viewBox="0 0 24 24" aria-hidden="true"><path d="M6.6 10.8a15.1 15.1 0 0 0 6.6 6.6l2.2-2.2a1 1 0 0 1 1-.25 11.4 11.4 0 0 0 3.6.57 1 1 0 0 1 1 1V20a1 1 0 0 1-1 1A17 17 0 0 1 3 4a1 1 0 0 1 1-1h3.5a1 1 0 0 1 1 1c0 1.25.2 2.45.57 3.57a1 1 0 0 1-.25 1z"/></svg>
        <span>+64 21 547 3162</span>
      </p>
      <p class="contact__line">
        <svg class="contact__icon" viewBox="0 0 24 24" aria-hidden="true"><path d="M2 5h20v14H2zm2 2v.5l8 5 8-5V7zm0 2.8V17h16V9.8l-8 5z"/></svg>
        <span>danicap@harwellcapital.co.nz</span>
      </p>
    </div>
  </section>

</main>
</body>
</html>
```